Window Company website re-design

We are creating a new website design for http://brindlepanes.com and we are going to be using wordpress for the site. The idea is to make it appeal to homeowners, more than half of the visitors will be female so the design must appeal to them with appropriate colors and shapes. Historically the website has been dark with a black background and the idea is to keep some of that but make it much brighter with textures and inviting colors.
Major competitors which we will mimic are the following in order of favorites:
http://www.harlowmeadow.com/ (this is something we really like because of the full width, call to action, easy to navigate, space for
http://www.quarrygateandyard.com/ (this is a nice wide design with a lot of great image space and call to actions)
http://www.refitbyoakridgeplu.com/ (the full width is nice here)
http://www.tidelinepanes.com/ (the slide over option showing the window is nice here.)
Others:
http://www.vorbek.com/
http://www.tosca.com/home/default.aspx
http://www.whitlockpanels.com/
https://www.glazeplanet.com/
http://www.dorset.com/

Brindle is the leader in the industry so they want a design that is going to portray that. The owners say that their competitors always copy what they do so this design must be cutting edge.

Important elements need to included:
1. Make the design convey very obviously they are a replacement window and door company.
2. Very clear “request a free estimate” call to action box on the homepage.
3. Area for the “Live Support” call to action
4. Navigation:

- Home
- Why Brindle
o Saves Dollars, Makes Sense
o We Have You Covered Start to Finish
o The Brindle Difference
o Pitfalls to Avoid
- Windows and Doors
o Windows
 Double Hung Windows
 Awning Windows
 Basement Hopper Windows
 Bow Windows
 Garden Windows
 Casement Windows
 Bay Windows
 Slider Windows
 Dead-Lite / Specialty / Transom
o Doors
 Storm Doors
 Brindle French Doors
 Patio Slider Doors
 Door Catalog
 Keypad Deadbolt
o Before and After
- About Us
o Testimonials
o Directions
o Warranty
o Employment
o Manufacturing process
o Home Shows
o Community Involvement
- Financing
- Commercial Division
- Careers
- Contact Us

Important elements for the Home Page:
1. Call to action – request a free quote
2. Awards
3. Live support
4. Guarantee
5. Featured testimonials
6. Press releases
7. Locations (Map?)

The attached photos can be used for the homepage images

Target Market(s)

The target market is middle income home owners who want good quality and great service.

Font styles to use
Sans Serif

Colors

Designer to choose colors to be used in the design.

Requirements
Must have
• We will need 2 designs, one for the homepage and the other for the inner pages.

2. Awards
3. Live support
4. Guarantee
5. Featured testimonials
6. Press releases
7. Locations (Map?)

```html
<!DOCTYPE html>
<html lang="en">
<head>
<meta charset="utf-8">
<title>Brindle — The Window People</title>
<link href="https://fonts.googleapis.com/css2?family=Open+Sans:wght@400;600;700&display=swap" rel="stylesheet">
<style>
:root{
  --ink:#1a1e25;
  --nav:#20262f;
  --blue:#1f5fa8;
  --blue-dark:#173f73;
  --accent:#3a8fe0;
  --text:#6b6f75;
  --heading:#2a5a98;
  --foot:#2c2f34;
  --foot-deep:#232529;
  --foot-text:#b9bcc1;
  --line:#e3e5e8;
}
*{box-sizing:border-box;margin:0;padding:0}
html,body{width:787px;height:1200px;overflow:hidden;background:#fff}
body{font-family:"Open Sans",Arial,sans-serif;color:var(--text);position:relative;font-size:7px}
.abs{position:absolute}
/* header */
.topbar{left:0;top:0;width:787px;height:50px;background:linear-gradient(#1f232b,#15181e)}
.brand{left:108px;top:10px;display:flex;align-items:center;gap:6px;color:#fff}
.brand .mark{width:26px;height:26px;border:2px solid #fff}
.brand .name{font-size:20px;font-weight:700;line-height:1}
.brand .tag{font-size:8px;font-weight:600;line-height:1.2}
.assist{display:flex;align-items:center;gap:7px;color:#fff;top:14px}
.assist .ico{width:18px;height:18px;border:1.5px solid #ccc;border-radius:3px;display:flex;align-items:center;justify-content:center}
.assist small{display:block;font-size:7.5px;color:#b8bcc3}
.assist b{font-size:11.5px;font-weight:700}
.quote-btn{left:613px;top:14px;width:68px;height:22px;background:linear-gradient(#3c86d6,#1d5ea8);border:1px solid #6aa7e6;border-radius:2px;color:#fff;text-align:center;font-size:7px;line-height:8.5px;padding-top:2px}
.quote-btn b{font-weight:700}
.mainnav{left:0;top:50px;width:787px;height:28px;background:linear-gradient(#29303b,#1a1f27);border-top:1px solid #333a45;display:flex;padding-left:104px}
.mainnav a{color:#6e9fd6;text-decoration:none;font-size:7.5px;line-height:27px;padding:0 15px;border-right:1px solid #1a1e25;box-shadow:1px 0 0 #39404b}
.mainnav a.home{padding:0 10px;color:#fff}
/* hero */
.hero{left:0;top:78px;width:787px;height:314px;background:linear-gradient(180deg,#a8a9a3 0%,#d9d6cd 40%,#b3a38c 75%,#7c6650 100%)}
.arrow{top:212px;width:30px;height:30px;background:rgba(20,24,30,.8);display:flex;align-items:center;justify-content:center}
.caption{left:104px;top:245px;width:316px;height:85px;background:rgba(20,26,38,.88);padding:12px 17px;color:#fff}
.caption h1{font-size:14.5px;font-weight:600;line-height:19px}
.caption h1 span{color:var(--accent)}
.caption p{font-size:7px;line-height:9.5px;margin-top:9px}
/* awards */
.awards{left:0;top:392px;width:787px;height:50px;background:#1b1f27}
.award{display:flex;gap:14px;align-items:center;top:399px;color:#fff}
.award .badge{width:36px;height:36px;background:#3a3e46;flex:none}
.award .badge.round{border-radius:50%;background:#b9a766;width:34px;height:34px}
.award h3{font-size:7.5px;font-weight:700;letter-spacing:.2px}
.award p{font-size:5.5px;color:#aeb2b8;line-height:8px}
.award em{font-size:5.5px;color:#aeb2b8;line-height:8px;display:block}
/* guarantee */
.guar-title{left:0;width:787px;top:472px;text-align:center;color:var(--heading);font-size:7.5px;font-weight:700}
.guar-text{left:0;width:787px;top:485px;text-align:center;font-size:7px}
.tile{top:515px;width:84px}
.tile .ph{height:36px}
.tile span{display:block;text-align:center;font-size:6px;margin-top:7px;letter-spacing:.3px}
h2.sec{font-size:7.5px;font-weight:700;color:var(--heading);letter-spacing:.2px}
.about p{font-size:6.8px;line-height:12px;margin-top:8px}
.why li{list-style:none;display:flex;align-items:center;gap:8px;font-size:7px;font-weight:600;color:#555a61;margin-top:8px}
.why li i{width:9px;height:9px;border-radius:50%;background:var(--blue-dark);display:flex;align-items:center;justify-content:center}
.video{top:741px;width:182px;height:108px;background:linear-gradient(#6b6a66,#3c3a38)}
.video .bar{position:absolute;left:0;bottom:0;width:100%;height:16px;background:#1d1d1d}
.video .prog{position:absolute;left:0;top:0;width:100%;height:3px;background:#444}
.video .prog i{display:block;width:18%;height:3px;background:#c11}
.video .time{position:absolute;left:45px;top:6px;font-size:5px;color:#ddd}
.upd{left:499px;width:186px;display:flex;gap:11px}
.upd .ph{width:46px;height:46px;flex:none}
.upd h4{font-size:7.2px;font-weight:600;color:#4a4f56}
.upd p{font-size:5.3px;line-height:7px;margin-top:5px}
.upd a{display:block;text-align:right;font-size:5.3px;color:var(--blue-dark);font-weight:700;margin-top:4px}
/* newsletter */
.news{left:0;top:874px;width:787px;height:44px;background:linear-gradient(#f4f5f6,#e9eaec);border-top:1px solid var(--line)}
.nl-title{font-size:8px;color:var(--blue);font-weight:600}
.nl-text{font-size:5.5px;margin-top:3px}
.field{background:#fff;border:1px solid #d4d6d9;font-size:5.5px;color:#999;padding:0 8px;display:flex;align-items:center}
.submit{background:linear-gradient(#5c8bc1,#3a6aa3);border:1px solid #2b5588;color:#fff;font-size:7.5px;font-weight:700;display:flex;align-items:center;justify-content:center}
/* footer */
.footer{left:0;top:918px;width:787px;height:247px;background:var(--foot)}
.divider{left:399px;width:1px;height:247px;background:#25282c;box-shadow:1px 0 0 #34373c}
.fh{font-size:7.5px;font-weight:700;color:#fff}
.frule{height:1px;background:#3d4046;margin-top:5px}
.ftext{font-size:6px;line-height:9px;color:var(--foot-text)}
.flist li{list-style:none;font-size:5.5px;color:#fff;margin-top:5px}
.flist li::before{content:"›";color:#999;margin-right:5px}
.contact-row{display:flex;gap:10px;align-items:center;font-size:5.5px;color:#fff}
.inp{background:#fff;border:1px solid #ccc;font-size:5.5px;color:#888;padding:5px 6px}
.send{background:linear-gradient(#5c7ea6,#3f5f87);color:#fff;font-size:6px;font-weight:700;display:flex;align-items:center;justify-content:center;border-radius:2px}
.social{width:16px;height:16px;border-radius:50%;background:#fff}
.bottom{left:0;top:1165px;width:787px;height:35px;background:var(--foot-deep)}
.legal{top:1181px;font-size:5.5px;color:#8b8e93}
</style>
</head>
<body>

<header>
  <div class="abs topbar"></div>
  <div class="abs brand">
    <div class="mark"></div>
    <div><div class="name">Brindle</div><div class="tag">“The Window People”</div></div>
  </div>
  <div class="abs assist" style="left:372px">
    <div class="ico"><svg width="10" height="10" viewBox="0 0 10 10"><circle cx="5" cy="3.3" r="2" fill="#ccc"/><path d="M1 10c0-3 2-4.5 4-4.5S9 7 9 10z" fill="#ccc"/></svg></div>
    <div><small>Need Assistance?</small><b>Live Support</b></div>
  </div>
  <div class="abs assist" style="left:485px">
    <div class="ico"><svg width="10" height="10" viewBox="0 0 10 10"><path d="M2 1l2 2-1 1.3c.6 1.2 1.5 2.1 2.7 2.7L7 6l2 2-1.3 1.5C4.5 9 1 5.5.5 2.3z" fill="#ccc"/></svg></div>
    <div><small>Call us today</small><b>(800) 555-0142</b></div>
  </div>
  <div class="abs quote-btn">Request<br><b>FREE QUOTE</b></div>
  <nav class="abs mainnav">
    <a class="home" href="#"><svg width="8" height="7" viewBox="0 0 8 7"><path d="M4 0L0 3.5h1V7h2.2V5h1.6v2H7V3.5h1z" fill="#fff"/></svg></a>
    <a href="#">Why Choose Brindle</a>
    <a href="#">Windows and Doors</a>
    <a href="#">About Us</a>
    <a href="#">Financing</a>
    <a href="#">Commercial Division</a>
    <a href="#">Careers</a>
    <a href="#" style="border:0;box-shadow:none">Contact Us</a>
  </nav>
</header>

<section>
  <div class="abs hero" role="img" aria-label="Bright living room with tall white-framed windows overlooking a harbor, a sofa and a television"></div>
  <div class="abs arrow" style="left:0"><svg width="8" height="12" viewBox="0 0 8 12"><path d="M6 1L1 6l5 5" stroke="#fff" stroke-width="1.5" fill="none"/></svg></div>
  <div class="abs arrow" style="left:757px"><svg width="8" height="12" viewBox="0 0 8 12"><path d="M2 1l5 5-5 5" stroke="#fff" stroke-width="1.5" fill="none"/></svg></div>
  <div class="abs caption">
    <h1>Replacing your home's windows with<br><span>high-performance.</span></h1>
    <p>For over 30 years we have been designing windows to fit your world, Brindle Windows is one of the wisest home improvement investments you'll ever make.</p>
  </div>
</section>

<section>
  <div class="abs awards"></div>
  <div class="abs award" style="left:156px">
    <div class="badge"></div>
    <div><h3>TOP COMPANY IN THE COUNTRY</h3><p>in the window category for three consecutive years.</p><em style="margin-top:3px">-Remodel Quarterly, most popular trade magazines</em></div>
  </div>
  <div class="abs award" style="left:405px">
    <div class="badge round"></div>
    <div><h3>BEST INTERNET SITE FOR A PRODUCT SUPPLIER</h3><em style="margin-top:3px">—by the Regional Home Builders Guild<br>of Eastbrook for 2012</em></div>
  </div>
</section>

<section>
  <div class="abs guar-title">OUR GUARANTEE: WE COVER EVERYTHING 100%.</div>
  <div class="abs guar-text">We are so confident in our work that we offer one of the best guarantees in the industry. We even cover labor and installation.</div>
  <div class="abs tile" style="left:106px"><div class="ph" role="img" aria-label="Red roofs of houses" style="background:linear-gradient(#b4473c,#e8e2dc)"></div><span>WINDOWS</span></div>
  <div class="abs tile" style="left:204px"><div class="ph" role="img" aria-label="Cracked glass pane" style="background:linear-gradient(#9aa3ab,#5b646c)"></div><span>GLASS BREAKAGE</span></div>
  <div class="abs tile" style="left:303px"><div class="ph" role="img" aria-label="Window frame seal" style="background:linear-gradient(90deg,#e9eef2,#aed0e8)"></div><span>SEALS</span></div>
  <div class="abs tile" style="left:403px"><div class="ph" role="img" aria-label="Store hours sign on a window" style="background:linear-gradient(#6b5a48,#3f3428)"></div><span>VINYL</span></div>
  <div class="abs tile" style="left:499px"><div class="ph" role="img" aria-label="Window hardware parts" style="background:linear-gradient(#c9c2b4,#8d8576)"></div><span>PARTS</span></div>
  <div class="abs tile" style="left:597px"><div class="ph" role="img" aria-label="Hard hat and plans on a table" style="background:linear-gradient(90deg,#e8c232,#b9c6d3)"></div><span>SERVICE</span></div>
</section>

<section>
  <div class="abs about" style="left:106px;top:602px;width:380px">
    <h2 class="sec">ABOUT OUR COMPANY</h2>
    <p>We offer a wide selection of top quality, custom-made windows to fit your home because we know you appreciate variety, expect quality and demand affordability.</p>
    <p style="margin-top:12px">Our windows are a reflection of our dedication and commitment to excellence. The skill and care our people take in manufacturing quality replacement windows originates from the tremendous pride we exhibit in all phases of production, including precise engineering and thorough quality control testing. All windows are made in the USA.</p>
  </div>
  <div class="abs why" style="left:499px;top:602px">
    <h2 class="sec" style="margin-bottom:4px">WHY CHOOSE US?</h2>
    <ul>
      <li><i><svg width="5" height="5" viewBox="0 0 5 5"><path d="M1.5 .5l2 2-2 2" stroke="#fff" fill="none"/></svg></i>Save dollars, make sense</li>
      <li><i><svg width="5" height="5" viewBox="0 0 5 5"><path d="M1.5 .5l2 2-2 2" stroke="#fff" fill="none"/></svg></i>We cover start to finish</li>
      <li><i><svg width="5" height="5" viewBox="0 0 5 5"><path d="M1.5 .5l2 2-2 2" stroke="#fff" fill="none"/></svg></i>Award winning services</li>
      <li><i><svg width="5" height="5" viewBox="0 0 5 5"><path d="M1.5 .5l2 2-2 2" stroke="#fff" fill="none"/></svg></i>We guarantee 100% satisfaction</li>
    </ul>
  </div>
</section>

<section>
  <h2 class="abs sec" style="left:105px;top:720px">WHAT OUR CLIENTS SAY ABOUT US</h2>
  <div class="abs video" style="left:106px" role="img" aria-label="Video testimonial from a customer">
    <div class="bar"><div class="prog"><i></i></div>
      <svg class="abs" style="left:12px;top:6px" width="6" height="7" viewBox="0 0 6 7"><path d="M0 0l6 3.5L0 7z" fill="#ccc"/></svg>
      <span class="time">0:02 / 4:17</span></div>
  </div>
  <div class="abs video" style="left:303px;background:linear-gradient(#8a8580,#4c4540)" role="img" aria-label="Video testimonial from a homeowner">
    <div class="bar"><div class="prog"><i></i></div>
      <svg class="abs" style="left:12px;top:6px" width="6" height="7" viewBox="0 0 6 7"><path d="M0 0l6 3.5L0 7z" fill="#ccc"/></svg>
      <span class="time">0:02 / 4:17</span></div>
  </div>
  <h2 class="abs sec" style="left:499px;top:720px">LATEST UPDATES</h2>
  <div class="abs upd" style="top:740px">
    <div class="ph" role="img" aria-label="Best of award certificate" style="background:linear-gradient(#f3e6a6,#e2cf7e)"></div>
    <div><h4>Irraer sit voluptatem accusantium</h4><p>Proin gravida nibh vel velit auctor aliquet. Aenean sollicitudin, lorem quis bibendum auctor, nisi elit consequat ipsum, nec sagittis sem nibh id elit.</p><a>Continue reading...</a></div>
  </div>
  <div class="abs upd" style="top:802px">
    <div class="ph" role="img" aria-label="House exterior with new windows" style="background:linear-gradient(#b8cbe0,#a88a6a)"></div>
    <div><h4>Irraer sit voluptatem accusantium</h4><p>Proin gravida nibh vel velit auctor aliquet. Aenean sollicitudin, lorem quis bibendum auctor, nisi elit consequat ipsum, nec sagittis sem nibh id elit.</p><a>Continue reading...</a></div>
  </div>
</section>

<section>
  <div class="abs news"></div>
  <div class="abs" style="left:183px;top:885px"><h3 class="nl-title">Subscribe to our Newsletter</h3><p class="nl-text">Sign up and stay updated. Get the latest new and special offers.</p></div>
  <div class="abs field" style="left:360px;top:886px;width:170px;height:19px">Enter Your Email Address</div>
  <div class="abs submit" style="left:530px;top:886px;width:55px;height:19px">Submit</div>
</section>

<footer>
  <div class="abs footer"></div>
  <div class="abs divider" style="top:918px"></div>

  <div class="abs" style="left:107px;top:954px;width:104px">
    <div class="fh">About Us</div><div class="frule"></div>
  </div>
  <div class="abs brand" style="left:108px;top:983px">
    <div class="mark"></div>
    <div><div class="name">Brindle</div><div class="tag">“The Window People”</div></div>
  </div>
  <p class="abs ftext" style="left:106px;top:1034px;width:105px">Vestibulum id ligula porta felis euismod semper. Integer posuere erat a ante.</p>

  <div class="abs" style="left:254px;top:954px;width:105px">
    <div class="fh">Contact Details</div><div class="frule"></div>
    <p class="ftext" style="margin-top:6px">There are many variations of passages of Lorem Ipsum available, but the majority have suffered alteration.</p>
  </div>
  <div class="abs contact-row" style="left:254px;top:1024px"><svg width="7" height="9" viewBox="0 0 7 9"><path d="M3.5 0A3.2 3.2 0 0 0 .3 3.2C.3 5.5 3.5 9 3.5 9s3.2-3.5 3.2-5.8A3.2 3.2 0 0 0 3.5 0zm0 4.5a1.3 1.3 0 1 1 0-2.6 1.3 1.3 0 0 1 0 2.6z" fill="#999"/></svg>New Delhi</div>
  <div class="abs contact-row" style="left:253px;top:1039px"><svg width="9" height="7" viewBox="0 0 9 7"><rect width="9" height="7" fill="#999"/><path d="M0 0l4.5 3.5L9 0" stroke="#2c2f34" fill="none"/></svg>info@yourwebsite.com</div>
  <div class="abs contact-row" style="left:254px;top:1053px"><svg width="8" height="8" viewBox="0 0 10 10"><path d="M2 1l2 2-1 1.3c.6 1.2 1.5 2.1 2.7 2.7L7 6l2 2-1.3 1.5C4.5 9 1 5.5.5 2.3z" fill="#999"/></svg>890-05550-12340</div>

  <div class="abs" style="left:105px;top:1081px">
    <div class="fh">Navigation</div>
    <ul class="flist"><li>Home</li><li>About</li><li>Services</li><li>Contact</li></ul>
  </div>
  <div class="abs" style="left:252px;top:1081px">
    <div class="fh">Services</div>
    <ul class="flist"><li>Menu1</li><li>Menu1</li><li>Menu1</li><li>Menu1</li></ul>
  </div>

  <div class="abs" style="left:435px;top:954px;width:246px">
    <div class="fh">We'd love to hear from you.</div>
    <p class="ftext" style="margin-top:7px">If you have questions or inquires, please don't hesitate to contact us through phone or you can send your message using the contact form below:</p>
  </div>
  <svg class="abs" style="left:668px;top:954px" width="12" height="9" viewBox="0 0 12 9"><ellipse cx="5" cy="4" rx="4.5" ry="3.3" fill="none" stroke="#888"/><ellipse cx="8" cy="5" rx="3.5" ry="2.7" fill="none" stroke="#888"/></svg>
  <div class="abs inp" style="left:435px;top:1000px;width:114px;height:17px">Name</div>
  <div class="abs inp" style="left:435px;top:1022px;width:114px;height:17px">Email</div>
  <div class="abs inp" style="left:435px;top:1045px;width:114px;height:17px">Phone</div>
  <div class="abs inp" style="left:559px;top:1000px;width:123px;height:62px">Message</div>
  <div class="abs send" style="left:627px;top:1073px;width:54px;height:18px">Send Email</div>

  <div class="abs fh" style="left:435px;top:1108px">Social Links</div>
  <div class="abs social" style="left:435px;top:1124px"></div>
  <div class="abs social" style="left:459px;top:1124px"></div>
  <div class="abs social" style="left:482px;top:1124px"></div>
  <div class="abs social" style="left:506px;top:1124px"></div>

  <div class="abs bottom"></div>
  <div class="abs legal" style="left:106px">Copyright 2014 © Brindle - All Rights Reserved</div>
  <div class="abs legal" style="left:560px">Site Map &nbsp;•&nbsp; Privacy Policy &nbsp;•&nbsp; Disclaimer</div>
</footer>

</body>
</html>
```